Marketing Booklet - Lumo Vastrel
12 Page Marketing Collateral - Ready for your design with images and content
Marketing Booklet - Lumo Vastrel - Financial Services
Creative Brief
Financial Services
This is a sales tool to banks to tell a story about the damage and risk of a disaster to their business and how our company can provide them preparedness and protection. Audience are bank executives and get bored easily. Tell the story with pictures and edgy design.
Front and back covers are largely created by a previous project and will not require much time. We need the full 12 pages created but we have provided the content, images and suggested layouts. We require your creative and talent to make this a unique booklet. It will be a landscape printed, heavy stock, glossy coat, booklet stapled on the small end. Pages need continuity in design because they will be printed touching each other. Finished product needs to be provided in multiple formats including jpeg, ai and a single PDF document that contains each of the 12 finished pages in order. Finished pages need to be 11 1/4 by 8 3/4 to accommodate the 1/8th inch trim.

```html
<!DOCTYPE html>
<html lang="en">
<head>
<meta charset="utf-8">
<title>Lumo Vastrel – Marketing Booklet Spreads</title>
<link rel="stylesheet" href="https://fonts.googleapis.com/css2?family=Open+Sans:wght@400;600;700;800&display=swap">
<style>
:root{
  --navy:#0b2a5a;
  --blue:#1b6fb3;
  --teal:#1b8fc9;
  --green:#7ab83c;
  --ink:#1d2a3a;
  --muted:#5a6675;
  --paper:#ffffff;
  --rule:#c9ced6;
  --label:#555;
}
*{box-sizing:border-box;margin:0;padding:0}
html,body{width:1200px;height:722px;overflow:hidden;background:#fff}
body{font-family:"Open Sans",Arial,sans-serif;color:var(--ink)}
.board{display:grid;grid-template-columns:repeat(4,287px);column-gap:13px;row-gap:22px;padding:10px 6px 0 9px}
.slot-label{font-size:8px;color:var(--label);height:12px;line-height:10px}
.page{position:relative;width:287px;height:200px;background:var(--paper);border:1px solid var(--rule);overflow:hidden}
.swoosh{position:absolute;left:0;bottom:0;width:287px;height:200px}
.abs{position:absolute}
.ph{position:absolute}
.tiny{font-size:5px;line-height:1.35;color:var(--muted)}
.h-navy{color:var(--navy);font-weight:800}
.h-blue{color:var(--blue);font-weight:700}
.brand{display:flex;align-items:center;gap:5px;color:var(--navy);font-weight:800;letter-spacing:.5px}
.brand .dot{border-radius:50%;background:var(--teal)}
.circle{border-radius:50%}
ul.bullets{list-style:none}
ul.bullets li{font-size:5px;line-height:1.5;color:var(--muted);padding-left:6px;position:relative}
ul.bullets li::before{content:"";position:absolute;left:0;top:2px;width:3px;height:3px;background:var(--teal)}
ul.checks{list-style:none}
ul.checks li{font-size:5.5px;line-height:1.9;color:var(--ink);padding-left:8px;position:relative}
ul.checks li::before{content:"";position:absolute;left:0;top:2px;width:5px;height:5px;border:1px solid var(--teal)}
table.stats{border-collapse:collapse;font-size:5px;color:var(--ink)}
table.stats td,table.stats th{border:1px solid var(--rule);padding:1px 4px}
table.stats th{background:var(--navy);color:#fff;font-weight:600}
</style>
</head>
<body>
<svg width="0" height="0" style="position:absolute">
  <defs>
    <symbol id="swoosh" viewBox="0 0 287 200" preserveAspectRatio="none">
      <path d="M0 178 C80 152 180 202 287 162 L287 200 L0 200Z" fill="#0b2a5a"/>
      <path d="M0 170 C90 146 180 192 287 152" stroke="#1b8fc9" stroke-width="3" fill="none"/>
      <path d="M0 184 C90 162 190 202 287 172" stroke="#7ab83c" stroke-width="2" fill="none"/>
    </symbol>
  </defs>
</svg>

<main class="board">

  <!-- Page 1: front cover -->
  <section class="slot">
    <div class="slot-label">Page 1</div>
    <div class="page cover-front">
      <div class="ph" role="img" aria-label="Soft grey wave background" style="inset:0;background:linear-gradient(160deg,#fff 30%,#e9edf2 70%,#fff)"></div>
      <p class="abs tiny" style="left:10px;top:8px;width:90px;color:var(--navy)">Trusted continuity and technology for financial institutions</p>
      <div class="abs brand" style="left:88px;top:88px;font-size:12px">
        <span class="dot" style="width:16px;height:16px"></span>LUMO VASTREL
      </div>
      <svg class="swoosh"><use href="#swoosh"/></svg>
    </div>
  </section>

  <!-- Page 2: photo collage -->
  <section class="slot">
    <div class="slot-label">Page 2</div>
    <div class="page collage">
      <div class="ph" role="img" aria-label="Flood damage photo" style="left:4px;top:4px;width:92px;height:60px;background:#8a8f95"></div>
      <div class="ph" role="img" aria-label="Collapsed building photo" style="left:98px;top:4px;width:92px;height:60px;background:#6e6a64"></div>
      <div class="ph" role="img" aria-label="Storm damage photo" style="left:192px;top:4px;width:91px;height:60px;background:#9aa4ad"></div>
      <div class="ph" role="img" aria-label="Fire at night photo" style="left:4px;top:66px;width:92px;height:60px;background:linear-gradient(#3a1e10,#c8601c)"></div>
      <div class="ph" role="img" aria-label="Damaged street photo" style="left:98px;top:66px;width:92px;height:60px;background:#7b7469"></div>
      <div class="ph" role="img" aria-label="Debris field photo" style="left:192px;top:66px;width:91px;height:60px;background:#a39a8c"></div>
      <div class="ph" role="img" aria-label="Power lines down photo" style="left:4px;top:128px;width:92px;height:58px;background:#b7b2a8"></div>
      <div class="ph" role="img" aria-label="Hurricane clouds photo" style="left:98px;top:128px;width:92px;height:58px;background:#5e6670"></div>
      <div class="ph" role="img" aria-label="Flooded office photo" style="left:192px;top:128px;width:91px;height:58px;background:#8b7f70"></div>
    </div>
  </section>

  <!-- Page 3 -->
  <section class="slot">
    <div class="slot-label">Page 3</div>
    <div class="page">
      <h2 class="abs h-navy" style="left:20px;top:6px;width:250px;font-size:9px;line-height:1.2;text-align:center">What would it take to separate you from your Office … your Data … your Customer</h2>
      <div class="ph circle" role="img" aria-label="Storm photo" style="left:22px;top:48px;width:42px;height:42px;background:#6d7a88"></div>
      <div class="ph circle" role="img" aria-label="Server room photo" style="left:70px;top:52px;width:38px;height:38px;background:#3e5c7a"></div>
      <div class="ph circle" role="img" aria-label="Hurricane satellite photo" style="left:114px;top:46px;width:46px;height:46px;background:#9aa9b6"></div>
      <div class="ph circle" role="img" aria-label="Fire photo" style="left:166px;top:52px;width:38px;height:38px;background:#b5561f"></div>
      <div class="ph circle" role="img" aria-label="Flooded road photo" style="left:210px;top:48px;width:42px;height:42px;background:#7f8b7a"></div>
      <p class="abs h-navy" style="left:20px;top:100px;width:250px;font-size:8px;text-align:center">There's a new word in Disaster Recovery.</p>
      <p class="abs" style="left:20px;top:112px;width:250px;font-size:8px;text-align:center;color:var(--blue);font-weight:700">It's … REALITY</p>
      <div class="ph" role="img" aria-label="Row of disaster photos" style="left:40px;top:128px;width:207px;height:22px;background:linear-gradient(90deg,#8a8f95,#6e6a64,#9aa4ad)"></div>
      <svg class="swoosh"><use href="#swoosh"/></svg>
    </div>
  </section>

  <!-- Page 4 -->
  <section class="slot">
    <div class="slot-label">Page 4</div>
    <div class="page">
      <svg class="abs" style="left:178px;top:6px" width="50" height="50" viewBox="0 0 50 50" aria-label="Pie chart of disaster types">
        <circle cx="25" cy="25" r="22" fill="#1b8fc9"/>
        <path d="M25 25 L25 3 A22 22 0 0 1 46 30Z" fill="#7ab83c"/>
        <path d="M25 25 L46 30 A22 22 0 0 1 20 47Z" fill="#e08a2a"/>
        <path d="M25 25 L20 47 A22 22 0 0 1 5 33Z" fill="#c0392b"/>
      </svg>
      <svg class="abs" style="left:232px;top:10px" width="46" height="46" viewBox="0 0 50 50" aria-label="Pie chart of losses">
        <circle cx="25" cy="25" r="22" fill="#0b2a5a"/>
        <path d="M25 25 L25 3 A22 22 0 0 1 44 36Z" fill="#9bc1e0"/>
        <path d="M25 25 L44 36 A22 22 0 0 1 12 43Z" fill="#7ab83c"/>
      </svg>
      <table class="stats abs" style="left:10px;top:12px">
        <tr><th colspan="2">Number of Disasters by Year</th></tr>
        <tr><td>2008</td><td>75</td></tr>
        <tr><td>2009</td><td>59</td></tr>
        <tr><td>2010</td><td>81</td></tr>
        <tr><td>2011</td><td>99</td></tr>
      </table>
      <p class="abs h-navy" style="left:150px;top:62px;font-size:10px">PROJECTED 2011</p>
      <p class="abs tiny" style="left:150px;top:76px;width:128px">declared natural disasters<br>forecast at record levels this year</p>
      <ul class="bullets abs" style="left:150px;top:92px;width:130px">
        <li>Severe storms hit every region</li>
        <li>Flooding closed many branches</li>
        <li>Outages lasted days not hours</li>
        <li>Power grid strain rose sharply</li>
        <li>Data loss remains the top risk</li>
      </ul>
      <div class="ph" role="img" aria-label="Tornado photo" style="left:10px;top:72px;width:128px;height:70px;background:linear-gradient(#5e6a78,#9aa2a8)"></div>
      <svg class="swoosh"><use href="#swoosh"/></svg>
    </div>
  </section>

  <!-- Page 5 -->
  <section class="slot">
    <div class="slot-label">Page 5</div>
    <div class="page">
      <svg class="abs" style="left:12px;top:10px" width="110" height="80" viewBox="0 0 110 80" aria-label="Pie chart of disaster losses">
        <ellipse cx="55" cy="44" rx="50" ry="30" fill="#0b2a5a"/>
        <ellipse cx="55" cy="40" rx="50" ry="30" fill="#1b8fc9"/>
        <path d="M55 40 L55 10 A50 30 0 0 1 104 44Z" fill="#e06a2a"/>
        <path d="M55 40 L104 44 A50 30 0 0 1 70 69Z" fill="#7ab83c"/>
        <path d="M55 40 L70 69 A50 30 0 0 1 20 62Z" fill="#b03a3a"/>
      </svg>
      <p class="abs h-navy" style="left:140px;top:12px;width:135px;font-size:8px;line-height:1.2">Over the past 50 years losses from disasters have exceeded $600 billion</p>
      <div class="ph" role="img" aria-label="Stacked coins photo" style="left:140px;top:48px;width:40px;height:34px;background:#7d8a80"></div>
      <p class="abs h-blue" style="left:186px;top:50px;width:92px;font-size:6.5px;line-height:1.25">First half of 2011 losses are $10 billion above the average historical</p>
      <p class="abs h-navy" style="left:12px;top:96px;width:150px;font-size:7px;line-height:1.2">Business Continuity Cannot Be a Game of Chance</p>
      <ul class="bullets abs" style="left:12px;top:116px;width:200px">
        <li>Regulators expect tested recovery plans for every critical system</li>
        <li>Customers leave when access to accounts is interrupted</li>
        <li>Recovery time decides whether a bank keeps its trust</li>
      </ul>
      <div class="ph" role="img" aria-label="Dice photo" style="left:220px;top:100px;width:55px;height:42px;background:#c9ced6"></div>
      <svg class="swoosh"><use href="#swoosh"/></svg>
    </div>
  </section>

  <!-- Page 6 -->
  <section class="slot">
    <div class="slot-label">Page 6</div>
    <div class="page">
      <div class="ph" role="img" aria-label="Falling dominoes photo" style="inset:0;background:linear-gradient(135deg,#2b2b2b,#6b6b6b 60%,#1a1a1a)"></div>
      <p class="abs" style="left:14px;top:96px;width:100px;font-size:7px;line-height:1.3;color:#fff;font-weight:700">Disasters need never happen. Whatever happens to your office and your data could be the first domino to fall.</p>
      <svg class="swoosh"><use href="#swoosh"/></svg>
    </div>
  </section>

  <!-- Page 7 -->
  <section class="slot">
    <div class="slot-label">Page 7</div>
    <div class="page">
      <div class="ph" role="img" aria-label="Bank vault and wood panelling photo" style="inset:0;background:linear-gradient(#5a3a24,#8a5a36 55%,#4a2e1c)"></div>
      <p class="abs" style="left:150px;top:10px;width:125px;font-size:10px;line-height:1.15;color:#fff;font-weight:800;text-align:right">When Fiduciary Failure is NOT an Option</p>
      <p class="abs" style="left:12px;top:118px;font-size:7px;color:#fff;font-weight:700">Mission Critical Services</p>
      <p class="abs tiny" style="left:12px;top:128px;width:150px;color:#f0e6da">Our teams keep core banking systems running through storms, fires and outages with tested plans and staffed recovery sites.</p>
      <svg class="swoosh"><use href="#swoosh"/></svg>
    </div>
  </section>

  <!-- Page 8 -->
  <section class="slot">
    <div class="slot-label">Page 8</div>
    <div class="page">
      <div class="ph" role="img" aria-label="Recovery center building with fountain photo" style="left:0;top:0;width:287px;height:110px;background:linear-gradient(#9bb7cf,#c8c2b4 60%,#8a8a7e)"></div>
      <p class="abs h-navy" style="left:160px;top:116px;font-size:8px">The Lumo Vastrel Center</p>
      <p class="abs tiny" style="left:160px;top:128px;width:118px">A hardened facility built to keep financial institutions open when their own buildings cannot.</p>
      <svg class="swoosh"><use href="#swoosh"/></svg>
    </div>
  </section>

  <!-- Page 9 -->
  <section class="slot">
    <div class="slot-label">Page 9</div>
    <div class="page">
      <p class="abs h-navy" style="left:10px;top:8px;font-size:8px">Our House</p>
      <p class="abs tiny" style="left:10px;top:19px;width:110px">Purpose built to withstand severe weather and power loss.</p>
      <p class="abs h-blue" style="left:10px;top:40px;font-size:6.5px">Quality Redundancies</p>
      <ul class="bullets abs" style="left:10px;top:50px;width:80px">
        <li>Dual power feeds</li><li>Backup generators</li><li>Fuel on site</li>
        <li>Fiber rings</li><li>Climate control</li><li>Fire suppression</li>
      </ul>
      <div class="ph" role="img" aria-label="Server racks photo" style="left:10px;top:110px;width:80px;height:40px;background:#2c3440"></div>
      <div class="ph" role="img" aria-label="Operations room photo" style="left:130px;top:8px;width:148px;height:40px;background:#6a7c8e"></div>
      <p class="abs h-navy" style="left:130px;top:54px;font-size:7px">Command Center</p>
      <p class="abs tiny" style="left:130px;top:64px;width:148px">Live monitoring of every client system around the clock.</p>
      <p class="abs h-navy" style="left:130px;top:84px;font-size:7px">Tier III Data Center</p>
      <p class="abs tiny" style="left:130px;top:94px;width:148px">Secure racks with redundant cooling and power.</p>
      <div class="ph" role="img" aria-label="Data hall photo" style="left:130px;top:106px;width:148px;height:40px;background:#3e4a58"></div>
      <svg class="swoosh"><use href="#swoosh"/></svg>
    </div>
  </section>

  <!-- Page 10 -->
  <section class="slot">
    <div class="slot-label">Page 10</div>
    <div class="page">
      <p class="abs h-navy" style="left:10px;top:8px;font-size:8px">Our House</p>
      <p class="abs tiny" style="left:10px;top:19px;width:120px">Private offices ready for your staff on day one.</p>
      <div class="ph circle" role="img" aria-label="Office interior photo" style="left:10px;top:34px;width:40px;height:40px;background:#a89a86"></div>
      <p class="abs h-navy" style="left:10px;top:84px;font-size:7px">Modular Offices</p>
      <p class="abs tiny" style="left:10px;top:94px;width:120px">Flexible seating that grows with your team.</p>
      <div class="ph circle" role="img" aria-label="Workstations photo" style="left:60px;top:104px;width:38px;height:38px;background:#8d9aa6"></div>
      <p class="abs h-navy" style="left:150px;top:8px;font-size:7px">Communications</p>
      <p class="abs tiny" style="left:150px;top:18px;width:128px">Phones and lines rerouted within minutes.</p>
      <div class="ph circle" role="img" aria-label="Telephone equipment photo" style="left:236px;top:32px;width:40px;height:40px;background:#4f6478"></div>
      <p class="abs h-navy" style="left:150px;top:84px;font-size:7px">Commercial Office Space</p>
      <p class="abs tiny" style="left:150px;top:94px;width:128px">Long term space for permanent recovery needs.</p>
      <div class="ph circle" role="img" aria-label="Office building photo" style="left:190px;top:106px;width:38px;height:38px;background:#b3b8be"></div>
      <svg class="swoosh"><use href="#swoosh"/></svg>
    </div>
  </section>

  <!-- Page 11 -->
  <section class="slot">
    <div class="slot-label">Page 11</div>
    <div class="page">
      <h2 class="abs h-navy" style="left:0;top:8px;width:287px;text-align:center;font-size:11px">The Core Package</h2>
      <p class="abs tiny" style="left:0;top:24px;width:287px;text-align:center">What you receive with every recovery agreement</p>
      <ul class="checks abs" style="left:24px;top:36px;width:110px">
        <li>Workspace seats</li><li>Data backup</li><li>Server hosting</li><li>Phone rerouting</li>
        <li>Mail handling</li><li>Staff training</li><li>Plan testing</li>
      </ul>
      <ul class="checks abs" style="left:150px;top:36px;width:110px">
        <li>Secure parking</li><li>Onsite security</li><li>Network access</li><li>Print services</li>
        <li>Vault storage</li><li>Help desk</li><li>Annual review</li>
      </ul>
      <svg class="swoosh"><use href="#swoosh"/></svg>
    </div>
  </section>

  <!-- Page 12: back cover -->
  <section class="slot">
    <div class="slot-label">Page 12</div>
    <div class="page cover-back">
      <div class="ph" role="img" aria-label="Soft grey wave background" style="inset:0;background:linear-gradient(200deg,#fff 30%,#e9edf2 70%,#fff)"></div>
      <p class="abs tiny" style="left:170px;top:10px;width:108px;text-align:right">Call today to schedule a tour of our recovery center.</p>
      <div class="abs" style="left:0;top:142px;width:287px;height:58px;background:var(--navy)"></div>
      <div class="abs brand" style="left:168px;top:150px;font-size:8px;color:#fff">
        <span class="dot" style="width:10px;height:10px"></span>LUMO VASTREL
      </div>
      <p class="abs tiny" style="left:168px;top:164px;width:110px;color:#cdd8e6">Continuity for financial institutions</p>
      <svg class="abs" style="left:0;top:120px" width="287" height="40" viewBox="0 0 287 40" preserveAspectRatio="none">
        <path d="M0 30 C90 0 190 40 287 14 L287 22 C190 48 90 8 0 40Z" fill="#1b8fc9"/>
        <path d="M0 36 C90 12 190 48 287 24" stroke="#7ab83c" stroke-width="2" fill="none"/>
      </svg>
    </div>
  </section>

</main>
</body>
</html>
```